PowerPoint Design

We require a sample PowerPoint design so we can pitch PPT design services to a client.

The designs do NOT need to be done in PowerPoint, but should reflect designs that *could* be created in PPT format.

We require 3 slides as part of this project:

1. A slide containing the statistical chart based on data in Figure 3.3 at http://data4.veltrondata.example/survey-releves/2006/ds-rs/fd-ft/index.cfm?LANG=ENG&VIEW=C&format=flash&PRCODE=01&TOPIC_ID=2
-> note, don't just copy and paste the existing graph - come up with something innovative and eye catching

2. Inspirational slide to motivate employees. Quorvix "inspirational quote" and select a quote you think is appropriate. Imagery should generate enthusiasm/optimism.

3. A slide of your own choosing.

Project Deadline Extended
Reason: One of the team reviewing the designs is away from office. We've decided to give other designers a chance to submit ideas. Final decision will be made on December 5th, 2011.

Target Market(s)

Business professionals

Industry/Entity Type

Quorvix

Requirements
Must have
• Must have 3 slides.

```html
<!DOCTYPE html>
<html lang="en">
<head>
<meta charset="utf-8">
<title>Agenda</title>
<link href="https://fonts.googleapis.com/css2?family=Carlito:wght@400;700&display=swap" rel="stylesheet">
<style>
  :root {
    --navy-deep: #06111f;
    --navy: #1a3d66;
    --blue: #3a78c0;
    --blue-light: #5b9be0;
    --paper: #ffffff;
    --rule: #c3dbe8;
    --margin-line: #f2c9c9;
    --ink: #1b2f4a;
    --accent: #e07d00;
    --logo-grey: #8c8c8c;
  }
  * { margin: 0; padding: 0; box-sizing: border-box; }
  html, body { width: 1200px; height: 900px; overflow: hidden; }
  body { font-family: "Carlito", "Calibri", sans-serif; }

  .slide {
    position: relative;
    width: 1200px;
    height: 900px;
    overflow: hidden;
    background:
      radial-gradient(ellipse 900px 700px at 1150px 80px, var(--blue-light) 0%, rgba(91,155,224,0) 70%),
      linear-gradient(120deg, var(--navy-deep) 0%, var(--navy) 35%, var(--blue) 75%, var(--blue-light) 100%);
  }

  .paper-shadow {
    position: absolute;
    left: 110px;
    top: 300px;
    width: 260px;
    height: 700px;
    background: rgba(5, 15, 30, 0.75);
    filter: blur(40px);
    transform: rotate(-5deg);
  }

  .paper {
    position: absolute;
    left: 175px;
    top: 210px;
    width: 1150px;
    height: 900px;
    transform: rotate(-4.8deg);
    transform-origin: 0 0;
    background-color: var(--paper);
    background-image:
      linear-gradient(to right, transparent 58px, var(--margin-line) 58px, var(--margin-line) 60px, transparent 60px),
      repeating-linear-gradient(to bottom, transparent 0, transparent 58px, var(--rule) 58px, var(--rule) 60px);
    background-position: 0 0, 0 22px;
    box-shadow: -6px 8px 24px rgba(0,0,0,0.35);
  }

  .title {
    position: absolute;
    top: 72px;
    left: 0;
    width: 1156px;
    text-align: center;
    color: #fff;
    font-weight: 700;
    font-size: 62px;
    letter-spacing: 1px;
  }

  .agenda {
    position: absolute;
    left: 333px;
    top: 252px;
    color: var(--ink);
  }
  .agenda-heading {
    font-size: 40px;
    font-weight: 400;
    margin-bottom: 42px;
  }
  .agenda-list { list-style: none; }
  .agenda-item {
    display: flex;
    align-items: center;
    height: 60px;
    font-size: 31px;
  }
  .agenda-item svg { width: 20px; height: 22px; margin-right: 14px; flex: none; }

  .date-badge {
    position: absolute;
    left: 872px;
    top: 107px;
    width: 230px;
    height: 230px;
    border-radius: 50%;
    background: var(--accent);
    box-shadow: 2px 6px 14px rgba(0,0,0,0.35);
    color: #fff;
    text-align: center;
  }
  .date-badge-text {
    position: absolute;
    inset: 0;
    transform: rotate(15deg);
    display: flex;
    flex-direction: column;
    align-items: center;
    justify-content: center;
    line-height: 1;
  }
  .date-day { font-size: 64px; font-weight: 400; margin-bottom: 2px; }
  .date-month { font-size: 36px; font-weight: 700; }
  .date-year { font-size: 34px; font-weight: 700; margin-top: 4px; }

  .logo-box {
    position: absolute;
    left: 1020px;
    top: 769px;
    width: 154px;
    height: 112px;
    background: #fff;
    box-shadow: 0 2px 8px rgba(0,0,0,0.3);
    display: flex;
    align-items: center;
    justify-content: center;
    color: var(--logo-grey);
    font-weight: 700;
    font-size: 44px;
    line-height: 0.92;
    text-align: left;
  }
</style>
</head>
<body>
  <div class="slide">
    <div class="paper-shadow"></div>
    <div class="paper"></div>

    <h1 class="title">AGENDA</h1>

    <section class="agenda">
      <h2 class="agenda-heading">Topic</h2>
      <ul class="agenda-list">
        <li class="agenda-item"><svg viewBox="0 0 20 22"><polygon points="2,1 19,11 2,21 6,11" fill="#e07d00"/></svg>Weekly Project/Team Updates</li>
        <li class="agenda-item"><svg viewBox="0 0 20 22"><polygon points="2,1 19,11 2,21 6,11" fill="#e07d00"/></svg>Functional Area #1 Status/Risk Updates</li>
        <li class="agenda-item"><svg viewBox="0 0 20 22"><polygon points="2,1 19,11 2,21 6,11" fill="#e07d00"/></svg>Functional Area #2 Status/Risk Updates</li>
        <li class="agenda-item"><svg viewBox="0 0 20 22"><polygon points="2,1 19,11 2,21 6,11" fill="#e07d00"/></svg>Functional Area #3 Status/Risk Updates</li>
        <li class="agenda-item"><svg viewBox="0 0 20 22"><polygon points="2,1 19,11 2,21 6,11" fill="#e07d00"/></svg>Communications</li>
        <li class="agenda-item"><svg viewBox="0 0 20 22"><polygon points="2,1 19,11 2,21 6,11" fill="#e07d00"/></svg>Upcoming Milestones</li>
        <li class="agenda-item"><svg viewBox="0 0 20 22"><polygon points="2,1 19,11 2,21 6,11" fill="#e07d00"/></svg>Folow-Ups/Next Steps</li>
        <li class="agenda-item"><svg viewBox="0 0 20 22"><polygon points="2,1 19,11 2,21 6,11" fill="#e07d00"/></svg>Other Items</li>
      </ul>
    </section>

    <div class="date-badge">
      <div class="date-badge-text">
        <span class="date-day">23</span>
        <span class="date-month">November</span>
        <span class="date-year">2011</span>
      </div>
    </div>

    <div class="logo-box">YOUR<br>LOGO</div>
  </div>
</body>
</html>
```